Cardiology practice business card

We need a business card for our cardiology practice "Bellmoor Cardiology". We have a new logo, attached below. We like the colours in the logo - red and charcoal. The front of the business card will need to have the doctors name, address, phone number and email. The back will need to have space to write 2 appointment dates and times.

```html
<!DOCTYPE html>
<html lang="en">
<head>
<meta charset="utf-8">
<title>Bellmoor Cardiology – Business Card</title>
<link href="https://fonts.googleapis.com/css2?family=Lato:wght@400;700;900&display=swap" rel="stylesheet">
<style>
  :root {
    --backdrop: #a5a5a5;
    --brand-red: #cc2026;
    --brand-red-deep: #a8171c;
    --accent-red: #e2332b;
    --charcoal: #3c3c3c;
    --ink: #1f1f1f;
    --paper: #ffffff;
  }
  * { margin: 0; padding: 0; box-sizing: border-box; }
  html, body { width: 1200px; height: 1000px; overflow: hidden; }
  body {
    position: relative;
    background: var(--backdrop);
    font-family: "Lato", Arial, sans-serif;
    color: var(--ink);
  }
  .card {
    position: absolute;
    left: 204px;
    width: 828px;
    height: 472px;
    border-radius: 20px;
  }
  .card-front { top: 17px; background: var(--brand-red); }
  .card-back { top: 504px; background: var(--paper); }

  .front-wordmark {
    position: absolute;
    left: 0; right: 0; top: 185px;
    text-align: center;
    font-weight: 900;
    font-size: 58px;
    letter-spacing: 3px;
    line-height: 1.05;
    color: var(--brand-red-deep);
    text-transform: uppercase;
  }

  .back-wordmark {
    position: absolute;
    right: 30px; top: 34px;
    display: flex; align-items: center; gap: 10px;
  }
  .back-wordmark .mark-dot {
    width: 14px; height: 14px; border-radius: 50%;
    background: var(--brand-red);
  }
  .back-wordmark .mark-name {
    font-weight: 700;
    font-size: 21px;
    letter-spacing: 1.5px;
    line-height: 1.1;
    color: var(--charcoal);
    text-transform: uppercase;
  }

  .doctor {
    position: absolute;
    left: 90px; top: 144px; width: 262px;
    text-align: center;
  }
  .doctor-name {
    font-weight: 900; font-size: 29px; color: var(--accent-red);
    letter-spacing: -0.3px;
  }
  .doctor-role { font-size: 20px; margin-top: 6px; }

  .contact-list {
    position: absolute; left: 424px; top: 124px;
    list-style: none;
  }
  .contact-item {
    display: flex; align-items: flex-start; gap: 14px;
    font-size: 22px; line-height: 26px; margin-bottom: 11px;
  }
  .contact-icon { flex: 0 0 26px; width: 26px; height: 26px; }

  .appointment-title {
    position: absolute; left: 0; right: 0; top: 308px;
    text-align: center;
    font-weight: 700; font-size: 22px; color: var(--accent-red);
    letter-spacing: 0.5px;
  }
  .hours {
    position: absolute; top: 355px; font-size: 19px; line-height: 26px;
  }
  .hours-left { left: 124px; text-align: right; }
  .hours-right { left: 412px; text-align: right; }
  .hours .day { color: var(--accent-red); }

  .stethoscope-area {
    position: absolute; left: 58px; top: 348px; width: 46px; height: 92px;
    border-radius: 20px;
    background: var(--charcoal);
    opacity: 0.85;
  }
  .timeline {
    position: absolute; left: 96px; top: 412px; width: 652px; height: 3px;
    background: var(--charcoal);
  }
  .heart-area {
    position: absolute; left: 722px; top: 393px; width: 48px; height: 40px;
    border-radius: 14px 14px 24px 24px;
    background: var(--accent-red);
  }
</style>
</head>
<body>

<section class="card card-front" aria-label="Card front">
  <div class="front-wordmark">Bellmoor<br>Cardiology</div>
</section>

<section class="card card-back" aria-label="Card back">
  <div class="back-wordmark">
    <span class="mark-dot"></span>
    <span class="mark-name">Bellmoor<br>Cardiology</span>
  </div>

  <div class="doctor">
    <div class="doctor-name">DR. AARON HALE</div>
    <div class="doctor-role">General Surgeon</div>
  </div>

  <ul class="contact-list">
    <li class="contact-item">
      <svg class="contact-icon" viewBox="0 0 26 26" aria-hidden="true">
        <rect x="1.5" y="1.5" width="23" height="23" rx="4" fill="none" stroke="#e2332b" stroke-width="2"/>
        <path d="M8 7c1-1 2-1 2.5 0l1 2c.3.7 0 1.2-.6 1.6-.4.3-.4.8 0 1.6.8 1.3 1.6 2.1 2.9 2.9.8.4 1.3.4 1.6 0 .4-.6.9-.9 1.6-.6l2 1c1 .5 1 1.5 0 2.5-1.5 1.5-4 1-7-2s-4-5.5-3-8z" fill="#e2332b"/>
      </svg>
      <span>044-555 010 246</span>
    </li>
    <li class="contact-item">
      <svg class="contact-icon" viewBox="0 0 26 26" aria-hidden="true">
        <rect x="1.5" y="1.5" width="23" height="23" rx="4" fill="none" stroke="#e2332b" stroke-width="2"/>
        <path d="M6 13l14-6-4 13-3-5z" fill="#e2332b"/>
      </svg>
      <span>hello@bellmoorheart.com</span>
    </li>
    <li class="contact-item">
      <svg class="contact-icon" viewBox="0 0 26 26" aria-hidden="true">
        <rect x="1.5" y="1.5" width="23" height="23" rx="4" fill="none" stroke="#e2332b" stroke-width="2"/>
        <path d="M13 20s-5-5-5-9a5 5 0 0110 0c0 4-5 9-5 9z" fill="none" stroke="#e2332b" stroke-width="2"/>
        <circle cx="13" cy="11" r="1.8" fill="#e2332b"/>
      </svg>
      <span>412 N Orchard Ave Halden,<br>FL 33590, 2750 S Lakeview<br>Trail Marlow, FL 33912</span>
    </li>
  </ul>

  <div class="appointment-title">APPOINTMENT</div>

  <div class="hours hours-left">
    <div><span class="day">Monday:</span> 6:00 PM to 8:00 PM</div>
    <div><span class="day">Friday:</span> 4:00 PM to 6:00 PM</div>
  </div>
  <div class="hours hours-right">
    <div><span class="day">Tuesday:</span> 6:00 PM to 8:00 PM</div>
    <div><span class="day">Wednesday:</span> 4:00 PM to 6:00 PM</div>
  </div>

  <div class="stethoscope-area" role="img" aria-label="Stethoscope illustration"></div>
  <div class="timeline"></div>
  <div class="heart-area" role="img" aria-label="Red heart illustration"></div>
</section>

</body>
</html>
```